Electrical Engineering Business Card Design

I need a business card design for an engineering consulting company based in Orlando, FL. I have had a logo created which the files are attached. We work primarily in the theme park and entertainment market sector but do projects in all market sectors. We have been serving Central Florida since 1994 and continue to strive to serve our clients and provide outstanding designs.
Industry/Entity Type
Theme Park

```html
<!DOCTYPE html>
<html lang="en">
<head>
<meta charset="utf-8">
<title>Voltbridge Associates, P.A. — Business Card</title>
<link rel="stylesheet" href="https://fonts.googleapis.com/css2?family=Oswald:wght@600&family=Arimo:wght@400;700&family=Questrial&display=swap">
<style>
  :root {
    --backdrop: #e6e7e8;
    --paper: #fdfdfd;
    --brand-green: #9dc063;
    --brand-green-soft: #b2cf85;
    --ink-dark: #3c3c3c;
    --ink-mid: #4a4a4a;
  }
  * { margin: 0; padding: 0; box-sizing: border-box; }
  html, body {
    width: 1200px;
    height: 720px;
    overflow: hidden;
    background: var(--backdrop);
  }
  .canvas {
    position: relative;
    width: 1200px;
    height: 720px;
    display: flex;
    align-items: center;
    justify-content: center;
    gap: 60px;
  }
  .card {
    position: relative;
    width: 520px;
    height: 297px;
    background: var(--paper);
    box-shadow: 0 2px 6px rgba(0,0,0,0.08);
    overflow: hidden;
  }
  /* Front side */
  .card-front {
    display: flex;
    align-items: center;
    justify-content: center;
  }
  .brand-mark {
    display: flex;
    align-items: center;
    gap: 18px;
  }
  .brand-mark__square {
    width: 46px;
    height: 46px;
    background: var(--brand-green-soft);
  }
  .brand-mark__name {
    font-family: "Oswald", sans-serif;
    font-weight: 600;
    font-size: 96px;
    line-height: 1;
    letter-spacing: 4px;
    color: var(--brand-green-soft);
  }
  /* Back side */
  .accent-band {
    position: absolute;
    left: 0;
    top: 26px;
    width: 470px;
    height: 30px;
    background: var(--brand-green);
  }
  .company {
    position: absolute;
    left: 74px;
    top: 86px;
  }
  .company__name {
    font-family: "Oswald", sans-serif;
    font-weight: 600;
    font-size: 34px;
    line-height: 1;
    color: var(--ink-dark);
    transform: scaleX(0.82);
    transform-origin: left center;
    white-space: nowrap;
  }
  .company__city {
    margin-top: 4px;
    font-family: "Arimo", sans-serif;
    font-weight: 700;
    font-size: 13px;
    letter-spacing: 4.5px;
    color: var(--ink-mid);
  }
  .contact-person {
    position: absolute;
    right: 28px;
    top: 178px;
    text-align: right;
  }
  .contact-person__name {
    font-family: "Questrial", sans-serif;
    font-size: 17px;
    letter-spacing: 3px;
    color: var(--ink-mid);
  }
  .contact-person__email {
    margin-top: 3px;
    font-family: "Questrial", sans-serif;
    font-size: 15px;
    color: var(--brand-green);
  }
  .mailing-address {
    position: absolute;
    left: 30px;
    bottom: 22px;
    font-family: "Arimo", sans-serif;
    font-size: 14px;
    line-height: 1.3;
    color: var(--ink-dark);
    list-style: none;
  }
</style>
</head>
<body>
  <main class="canvas">
    <section class="card card-front" aria-label="Card front">
      <div class="brand-mark">
        <span class="brand-mark__square" aria-hidden="true"></span>
        <span class="brand-mark__name">VBA</span>
      </div>
    </section>

    <section class="card card-back" aria-label="Card back">
      <div class="accent-band" aria-hidden="true"></div>
      <div class="company">
        <h1 class="company__name">Voltbridge Associates, P.A.</h1>
        <p class="company__city">ORLANDO, FLORIDA</p>
      </div>
      <div class="contact-person">
        <p class="contact-person__name">DANA WHITFIELD</p>
        <p class="contact-person__email">dana@voltbridge-pa.com</p>
      </div>
      <ul class="mailing-address">
        <li>P.O. Box 410227</li>
        <li>Orlando, FL 32801</li>
        <li>407.555.0148</li>
      </ul>
    </section>
  </main>
</body>
</html>
```